Refresh Application User Interface

Brindlecove wishes to update the look of its business applications. Two representative forms are shown below. Please note, we are not considering changes in functionality or usability. Our goal is a cleaner, more contemporary design.

Industry/Entity Type

Business

```html
<!DOCTYPE html>
<html lang="en">
<head>
<meta charset="utf-8">
<title>Purchase Order Lines</title>
<link href="https://fonts.googleapis.com/css2?family=Nunito+Sans:wght@300;400;600;700;800&display=swap" rel="stylesheet">
<style>
:root{
  --topbar:#3d3d3d;--topbar-active:#c4c4c4;--nav-blue:#4a8ff2;--brand:#1e5fb4;
  --page:#ebebeb;--panel:#ffffff;--soft:#f6f6f6;--line:#dcdcdc;--text:#444;
  --muted:#777;--link:#2455d8;--green:#1fb14f;--green-bar:#55c77a;--red:#e33;--field:#bdbdbd;
}
*{box-sizing:border-box;margin:0;padding:0}
html,body{width:1200px;height:756px;overflow:hidden}
body{font-family:"Nunito Sans",sans-serif;background:var(--page);color:var(--text);position:relative}
.abs{position:absolute}
.topbar{left:0;top:0;width:1200px;height:32px;background:var(--topbar);color:#fff}
.user{left:13px;top:7px;font-size:15px;font-weight:600}
.role{left:149px;top:9px;font-size:13px;font-weight:700}
.toplinks{right:0;top:0;display:flex;height:32px}
.toplinks span{font-size:11px;padding:0 18px;line-height:32px;color:#eee}
.toplinks .on{background:var(--topbar-active);color:#555}
.mainnav{left:0;top:32px;width:1200px;height:41px;background:#fff;display:flex}
.mainnav span{font-size:11px;color:#777;line-height:41px;text-align:center;border-right:1px solid #e5e5e5}
.mainnav .on{background:var(--nav-blue);color:#fff;font-weight:700}
.brand{right:18px;top:38px;font-size:24px;font-weight:800;color:var(--brand);letter-spacing:.5px}
.subnav{left:0;top:73px;width:1200px;height:29px;background:var(--nav-blue)}
.subnav span{position:absolute;top:8px;font-size:10px;color:#fff}
.subnav .on{font-weight:700;border-bottom:2px solid #fff;padding:0 24px 6px;top:8px}
.title{left:148px;top:130px;font-size:19px;color:#6b7a8c;font-weight:400}
.tab{top:126px;height:32px;background:#fff;border:1px solid var(--line);border-bottom:none;font-size:12px;color:#888;text-align:center;line-height:32px;letter-spacing:.3px}
.tab.on{top:118px;height:40px;background:var(--nav-blue);color:#fff;font-size:13px;line-height:40px;border:none}
.panel{left:149px;top:158px;width:901px;height:543px;background:var(--panel);box-shadow:0 1px 2px rgba(0,0,0,.15)}
.bar{left:0;width:901px;height:30px;background:#fff;border-bottom:1px solid var(--line)}
.bar .flag{position:absolute;left:0;top:0;width:8px;height:30px}
.tool-label{top:8px;font-size:11px;color:#444;white-space:nowrap}
.sep{left:210px;top:4px;width:1px;height:22px;background:var(--line)}
.info{left:0;top:30px;width:901px;height:138px;background:var(--soft);text-align:center}
.info .num{margin-top:24px;font-size:13px;color:#777}
.info .kind{font-size:18px;color:var(--green);font-weight:700;margin-top:5px}
.info .vendor{font-size:12.5px;color:#444;margin-top:22px}
.colhead{top:356px;font-size:10px;color:#666}
.row2bg{left:149px;top:478px;width:901px;height:88px;background:#f5f5f5}
.ln{font-size:12px;color:var(--link)}
.field{height:19px;border:1px solid var(--field);background:#fff;font-size:10px;line-height:18px;padding-left:7px;color:#444;border-radius:2px;white-space:nowrap;overflow:hidden}
.sel::after{content:"";position:absolute;right:8px;top:7px;border:4px solid transparent;border-top:5px solid #999}
.cb{width:12px;height:12px;border:1px solid #999;background:#fff}
.dollar{font-size:13px;color:#555}
.note{font-size:10px;color:#333}
.status{left:149px;top:715px;width:901px;height:25px;background:#fff;font-size:10.5px;color:#555;padding-left:25px;line-height:25px}
.status .flag{position:absolute;left:0;top:0;width:8px;height:25px;background:var(--green-bar)}
svg{display:block}
</style>
</head>
<body>
<div class="abs topbar">
  <div class="abs user">Dana Whitfield <svg style="display:inline-block;vertical-align:-2px" width="14" height="14" viewBox="0 0 14 14"><circle cx="7" cy="7" r="5" fill="none" stroke="#fff" stroke-width="3" stroke-dasharray="2 1.6"/><circle cx="7" cy="7" r="2" fill="#fff"/></svg></div>
  <div class="abs role">Administrator ⌄</div>
  <div class="abs toplinks"><span>TOUCH</span><span class="on">NEW TAB</span><span>HELP</span><span>SUPPORT</span><span><svg width="18" height="16" viewBox="0 0 18 16"><rect x="1" y="1" width="8" height="14" fill="none" stroke="#fff" stroke-width="1.5"/><path d="M8 8h9M14 5l3 3-3 3" stroke="#fff" stroke-width="1.5" fill="none"/></svg></span></div>
</div>
<nav class="abs mainnav">
  <span style="width:86px">Home</span><span style="width:93px">eSource</span><span class="on" style="width:80px">eBuy</span><span style="width:99px">eRequest</span><span style="width:77px">eSell</span><span style="width:86px">eStock</span><span style="width:80px">ePlan</span><span style="width:108px">Preferences</span>
</nav>
<div class="abs brand">BRINDLECOVE</div>
<div class="abs subnav">
  <span class="on" style="left:199px;padding:0 24px 6px">Orders</span>
  <span style="left:300px">Recepients</span><span style="left:388px">Shipments</span>
  <span style="left:455px;top:6px">|</span>
  <span style="left:475px">Invoices</span><span style="left:559px">Pricing</span><span style="left:629px">Tables</span><span style="left:697px">Reports</span><span style="left:771px">Inquiries</span><span style="left:849px">Periodic Tasks</span><span style="left:951px">Workflows</span>
</div>
<h1 class="abs title">PURCHASE ORDER LINES</h1>
<div class="abs tab" style="left:712px;width:81px">HEADER</div>
<div class="abs tab on" style="left:794px;width:92px">LINES</div>
<div class="abs tab" style="left:888px;width:81px">CHARGES</div>
<div class="abs tab" style="left:970px;width:81px">NOTES<svg class="abs" style="right:2px;top:2px" width="12" height="12" viewBox="0 0 12 12"><circle cx="6" cy="6" r="6" fill="var(--green)"/><path d="M3 6l2 2 4-4" stroke="#fff" stroke-width="1.5" fill="none"/></svg></div>

<div class="abs panel">
  <div class="abs bar" style="top:0">
    <div class="flag" style="background:var(--green-bar)"></div>
    <svg class="abs" style="left:30px;top:8px" width="170" height="15" viewBox="0 0 170 15" fill="none" stroke="#555" stroke-width="1.6">
      <path d="M5 3l6 6a2 2 0 0 1-3 3L2 6a3 3 0 0 1 5-4l6 6"/>
      <path d="M44 2l6 5-5 6-4-4z"/>
      <circle cx="81" cy="11" r="2" fill="#555"/><circle cx="88" cy="4" r="2" fill="#555"/><circle cx="92" cy="10" r="2" fill="#555"/><path d="M81 11l7-7 4 6"/>
      <rect x="118" y="5" width="13" height="8" fill="#555"/><rect x="122" y="2" width="5" height="3"/>
      <circle cx="157" cy="8" r="6" fill="#ccc" stroke="none"/>
    </svg>
    <div class="abs sep"></div>
    <svg class="abs" style="left:225px;top:9px" width="13" height="13" viewBox="0 0 13 13" fill="none" stroke="#555" stroke-width="1.6"><path d="M1 1l11 11M12 1L1 12"/></svg>
    <span class="abs tool-label" style="left:243px">View GL Accounts</span>
    <svg class="abs" style="left:353px;top:10px" width="13" height="11" viewBox="0 0 13 11"><rect width="13" height="11" fill="#444"/><circle cx="6.5" cy="5.5" r="2.5" fill="#fff"/></svg>
    <span class="abs tool-label" style="left:371px">Post Order</span>
    <svg class="abs" style="left:780px;top:8px" width="14" height="14" viewBox="0 0 14 14" fill="none" stroke="#2a8ad8" stroke-width="2"><circle cx="5.5" cy="5.5" r="4"/><path d="M8.5 8.5l4.5 4.5"/></svg>
    <svg class="abs" style="left:809px;top:8px" width="14" height="14" viewBox="0 0 14 14" fill="none" stroke="#ccc" stroke-width="2.4"><path d="M7 1v12M1 7h12"/></svg>
    <svg class="abs" style="left:838px;top:8px" width="16" height="14" viewBox="0 0 16 14" fill="none" stroke="var(--green)" stroke-width="2.4"><path d="M1 8l5 5 9-11"/></svg>
    <svg class="abs" style="left:869px;top:8px" width="13" height="13" viewBox="0 0 13 13" fill="none" stroke="var(--red)" stroke-width="2.4"><path d="M1 1l11 11M12 1L1 12"/></svg>
    <svg class="abs" style="left:895px;top:8px" width="14" height="14" viewBox="0 0 14 14" fill="none" stroke="var(--green)" stroke-width="1.6"><path d="M3 4h6a4 4 0 0 1 0 8H5M5 1L2 4l3 3"/></svg>
  </div>
  <div class="abs info">
    <div class="num">Order #&nbsp; 100159</div>
    <div class="kind">Regular Purchase Order</div>
    <div class="vendor">Harborline Supply Co., Eastbrook MA</div>
  </div>
  <div class="abs bar" style="top:168px;border-top:1px solid var(--line)">
    <div class="flag" style="background:var(--nav-blue)"></div>
    <span class="abs" style="left:32px;top:5px;font-size:15px;color:#444">Σ</span>
    <svg class="abs" style="left:68px;top:7px" width="130" height="15" viewBox="0 0 130 15" fill="none" stroke="#444" stroke-width="1.4">
      <rect x="4" y="3" width="8" height="11"/><path d="M1 11V1h8"/>
      <rect x="41" y="3" width="9" height="11" fill="#444"/><path d="M38 11V1h8"/>
      <path d="M80 2h14l-5 6v6l-4-2V8z" fill="#444"/>
      <path d="M112 2l10 10M122 2l-10 10" stroke="var(--red)" stroke-width="2.4"/>
    </svg>
    <svg class="abs" style="left:661px;top:9px" width="60" height="13" viewBox="0 0 60 13" fill="#999"><rect x="1" y="0" width="2" height="13"/><path d="M14 0v13L4 6.5z"/><path d="M50 0v13L42 6.5zM58 0v13L50 6.5z"/></svg>
    <span class="abs" style="left:743px;top:8px;font-size:11px;color:#555">Page 1 of 1</span>
    <svg class="abs" style="left:834px;top:9px" width="60" height="13" viewBox="0 0 60 13" fill="#999"><path d="M2 0v13l8-6.5zM10 0v13l8-6.5z"/><path d="M44 0v13l10-6.5z"/><rect x="55" y="0" width="2" height="13"/></svg>
  </div>
</div>

<span class="abs colhead" style="left:163px;top:362px">Line #</span>
<span class="abs colhead" style="left:224px;top:362px">Product</span>
<span class="abs colhead" style="left:359px;top:363px">Supplier Part #</span>
<span class="abs colhead" style="left:470px;top:362px">Open Qty</span>
<span class="abs colhead" style="left:564px;top:362px">Unit</span>
<span class="abs colhead" style="left:658px;top:362px">Unit Price</span>
<span class="abs colhead" style="left:750px;top:362px">Extended</span>
<span class="abs colhead" style="left:847px;top:362px">LI Type / Ship To</span>
<div class="abs cb" style="left:1013px;top:363px"></div>

<div class="abs row2bg"></div>

<span class="abs ln" style="left:163px;top:406px">10</span>
<div class="abs field" style="left:218px;top:403px;width:123px">P-1200</div>
<svg class="abs" style="left:343px;top:405px" width="14" height="14" viewBox="0 0 14 14" fill="none" stroke="#2a8ad8" stroke-width="1.8"><circle cx="8.5" cy="5.5" r="4"/><path d="M5.5 8.5L1 13"/></svg>
<div class="abs cb" style="left:373px;top:407px"></div>
<div class="abs field" style="left:466px;top:403px;width:70px">1</div>
<div class="abs field sel" style="left:561px;top:403px;width:70px"></div>
<span class="abs dollar" style="left:646px;top:404px">$</span>
<div class="abs field" style="left:657px;top:403px;width:70px">6.50</div>
<div class="abs field" style="left:218px;top:426px;width:508px">Papercrest 472105 - Brochure Paper, Ultra Smooth Text, 8 1/2” x 11”, 28 lb., 96 Brightness</div>
<div class="abs field sel" style="left:846px;top:404px;width:138px"></div>
<div class="abs field sel" style="left:846px;top:426px;width:138px"></div>
<div class="abs cb" style="left:1013px;top:407px"></div>
<span class="abs note" style="left:273px;top:454px">On Purchase Order&nbsp; <span style="color:var(--link)">&nbsp;30</span></span>
<span class="abs note" style="left:470px;top:453px">Available&nbsp; 0</span>
<span class="abs note" style="left:659px;top:452px;color:var(--red);font-style:italic">Over Budget</span>

<span class="abs ln" style="left:163px;top:491px">20</span>
<div class="abs field" style="left:218px;top:489px;width:123px">P-1200</div>
<svg class="abs" style="left:343px;top:490px" width="14" height="14" viewBox="0 0 14 14" fill="none" stroke="#2a8ad8" stroke-width="1.8"><circle cx="8.5" cy="5.5" r="4"/><path d="M5.5 8.5L1 13"/></svg>
<div class="abs cb" style="left:373px;top:492px"></div>
<div class="abs field" style="left:466px;top:489px;width:70px">1</div>
<div class="abs field sel" style="left:561px;top:489px;width:70px"></div>
<span class="abs dollar" style="left:646px;top:489px">$</span>
<div class="abs field" style="left:657px;top:489px;width:70px">6.50</div>
<div class="abs field" style="left:218px;top:512px;width:508px">Papercrest 472105 - Brochure Paper, Ultra Smooth Text, 8 1/2” x 11”, 28 lb., 96 Brightness</div>
<div class="abs field sel" style="left:846px;top:489px;width:138px"></div>
<div class="abs field sel" style="left:846px;top:512px;width:138px"></div>
<div class="abs cb" style="left:1013px;top:492px"></div>

<span class="abs ln" style="left:163px;top:577px">20</span>
<div class="abs field" style="left:218px;top:574px;width:123px"></div>
<svg class="abs" style="left:343px;top:576px" width="14" height="14" viewBox="0 0 14 14" fill="none" stroke="#2a8ad8" stroke-width="1.8"><circle cx="8.5" cy="5.5" r="4"/><path d="M5.5 8.5L1 13"/></svg>
<div class="abs cb" style="left:373px;top:578px"></div>
<div class="abs field" style="left:466px;top:574px;width:70px"></div>
<div class="abs field sel" style="left:561px;top:574px;width:70px"></div>
<span class="abs dollar" style="left:646px;top:575px">$</span>
<div class="abs field" style="left:657px;top:574px;width:70px"></div>
<div class="abs field" style="left:218px;top:597px;width:508px"></div>
<div class="abs field sel" style="left:846px;top:575px;width:138px"></div>
<div class="abs field sel" style="left:846px;top:597px;width:138px"></div>

<div class="abs status"><div class="flag"></div>Click <svg style="display:inline-block;vertical-align:-2px" width="12" height="12" viewBox="0 0 12 12" fill="none" stroke="#2a8ad8" stroke-width="1.8"><circle cx="5" cy="5" r="3.6"/><path d="M7.5 7.5L11 11"/></svg>Search, or enter property values and click <svg style="display:inline-block;vertical-align:-1px" width="13" height="11" viewBox="0 0 13 11" fill="none" stroke="var(--green)" stroke-width="2"><path d="M1 6l4 4 7-9"/></svg>Apply</div>
</body>
</html>
```